Want a package created for a new protein bar

We would like a new package created for a new protein bar project The name of the bar will be VOLMBite a real food protein bar, we would like a ‘window’ on the package of bar like Brave Meadow bar below in images.

VOLMBite
‘Super Food Bar’
14g of Whey Protein
The package film size is the following 12cm width x 15cm Length,
Flavor Peanut Chocolate Chip, additional information will be attached shortly like nutrition facts,

Target Market(s)

fitness market, bodybuilders, athletes, everyday people

Industry/Entity Type

Health Product

Logo Text

VOLMBite

Font styles to use
Serif
Sans Serif
Decorative

Requirements
Must have
• Package window

```html
<!DOCTYPE html>
<html lang="en">
<head>
<meta charset="UTF-8">
<title>VOLMBite – Peanut Chocolate Chip Wrapper</title>
<link href="https://fonts.googleapis.com/css2?family=Libre+Baskerville:wght@700&display=swap" rel="stylesheet">
<style>
  :root {
    --page: #f4ece3;
    --wrapper-orange: #e8884a;
    --wrapper-light: #f4b184;
    --wrapper-deep: #c9652c;
    --band-red: #f21a16;
    --band-edge: #a3120f;
    --ink-red: #b10c0c;
    --logo-white: #f8e8e6;
    --info-white: #fff4ec;
    --bar-tan: #c9a46e;
    --bar-light: #e2c9a0;
  }
  html, body {
    margin: 0;
    padding: 0;
    width: 1200px;
    height: 1200px;
    overflow: hidden;
    background: var(--page);
  }
  .canvas {
    position: relative;
    width: 1200px;
    height: 1200px;
  }
  .wrapper {
    position: absolute;
    left: 80px;
    top: 419px;
    width: 1040px;
    height: 362px;
    font-family: "Libre Baskerville", Georgia, serif;
    font-weight: 700;
  }
  .wrapper-shape {
    position: absolute;
    inset: 0;
  }
  .wrapper p,
  .wrapper h1 {
    position: absolute;
    margin: 0;
    line-height: 1;
    white-space: nowrap;
    font-weight: 700;
  }
  .flavor {
    left: 123px;
    top: 84px;
    font-size: 29px;
    color: var(--ink-red);
  }
  .brand-name {
    left: 123px;
    top: 145px;
    font-size: 62px;
    color: var(--logo-white);
  }
  .protein {
    left: 103px;
    top: 253px;
    font-size: 29px;
    color: var(--ink-red);
  }
  .nutrition-line {
    left: 526px;
    top: 32px;
    font-size: 21px;
    color: var(--info-white);
  }
  .net-weight {
    left: 594px;
    top: 306px;
    font-size: 21px;
    color: var(--info-white);
  }
</style>
</head>
<body>
<main class="canvas">
  <section class="wrapper" aria-label="VOLMBite Peanut Chocolate Chip protein bar wrapper">
    <svg class="wrapper-shape" viewBox="0 0 1040 362" width="1040" height="362" xmlns="http://www.w3.org/2000/svg">
      <defs>
        <linearGradient id="film" x1="0" y1="0" x2="0" y2="1">
          <stop offset="0" stop-color="var(--wrapper-light)"/>
          <stop offset="0.18" stop-color="var(--wrapper-orange)"/>
          <stop offset="0.85" stop-color="var(--wrapper-orange)"/>
          <stop offset="1" stop-color="var(--wrapper-deep)"/>
        </linearGradient>
        <radialGradient id="bar-fill" cx="0.5" cy="0.5" r="0.6">
          <stop offset="0" stop-color="var(--bar-light)"/>
          <stop offset="1" stop-color="var(--bar-tan)"/>
        </radialGradient>
      </defs>
      <path class="seal-left" fill="var(--wrapper-deep)" d="M0 6 L34 0 L34 362 L0 356 L6 340 L0 320 L6 300 L0 280 L6 260 L0 240 L6 220 L0 200 L6 180 L0 160 L6 140 L0 120 L6 100 L0 80 L6 60 L0 40 L6 20 Z"/>
      <path class="seal-right" fill="var(--wrapper-deep)" d="M1040 6 L1006 0 L1006 362 L1040 356 L1034 340 L1040 320 L1034 300 L1040 280 L1034 260 L1040 240 L1034 220 L1040 200 L1034 180 L1040 160 L1034 140 L1040 120 L1034 100 L1040 80 L1034 60 L1040 40 L1034 20 Z"/>
      <rect class="film-body" x="30" y="4" width="980" height="354" rx="10" fill="url(#film)"/>
      <rect class="band" x="30" y="128" width="980" height="95" fill="var(--band-red)"/>
      <line x1="30" y1="128" x2="1010" y2="128" stroke="var(--band-edge)" stroke-width="2"/>
      <line x1="30" y1="223" x2="1010" y2="223" stroke="var(--band-edge)" stroke-width="2"/>
      <rect class="window-frame" x="521" y="91" width="365" height="197" rx="98" fill="var(--band-red)" stroke="var(--band-edge)" stroke-width="4"/>
      <rect class="window" x="532" y="102" width="343" height="175" rx="87" fill="url(#bar-fill)" role="img" aria-label="Window showing the peanut chocolate chip bar inside"/>
    </svg>
    <p class="nutrition-line">? Net Carbs / ? Sugar / ?g Fiber</p>
    <p class="flavor">Peanut Chocolate Chip</p>
    <h1 class="brand-name">VOLMBite</h1>
    <p class="protein">14g of Whey Protein</p>
    <p class="net-weight">Net Wt. 2.12 Oz.</p>
  </section>
</main>
</body>
</html>
```